Recipe mobile app, new flow and design for uploading recipe process

I need a new recipe upload process that's simple, intuitive, and engaging.
The goal is to have a user-friendly and fast flow.
The app is a social recipe library where anyone can upload a recipe after signing up. I currently have a flow, but it's "boring," so I'd like to significantly improve this aspect of the app.
When I create a new recipe, it's immediately saved and labeled as a draft. I'll then need to specify:
- Recipe title
- Cover image (required)
- Number of people (how many people is the recipe for)
- Ingredients (name, quantity, and unit of measurement)
- Recipe explanation (broken down into steps, and I can optionally attach an image to each step)
- Upload
Every change is immediately saved, so you can edit, exit, and resume editing later.
I've attached images of the app and the current upload process.
Thank you.
Low design quality
Good morning everyone,
some of the designs received are fantastic, but please make sure to carefully read the requirement so as not to do extra work.
The requirement is to redesign the flow that a user follows when uploading a recipe to the platform.
We have uploaded the current app screens to give you an idea of what the product looks like, what the colors and style are, but we don’t need a full redesign - only the part mentioned above, while keeping the existing style and colors (we cannot rework the entire theme).
To clarify: if you look at the screens shared in the zip file attached to the project, the focus should be on the screens from 5_.png to 10_.png.
These screens can be redesigned in the most creative way you think, as long as the overall theme remains unchanged.
Thank you for your attention.

```html
<!DOCTYPE html>
<html lang="en">
<head>
<meta charset="UTF-8">
<title>New Recipe – Upload Flow</title>
<link rel="stylesheet" href="https://fonts.googleapis.com/css2?family=Inter:wght@400;500;600&display=swap">
<style>
  :root{
    --bg:#d8d6d5;
    --screen:#f5f5f6;
    --ink:#26272b;
    --label:#5a5c63;
    --muted:#6d6f75;
    --line:#e2e3e6;
    --field:#f7f7f8;
    --link:#2f7be6;
    --upload-ink:#2b6fb2;
    --upload-line:#3a6eb3;
    --upload-bg:#e3e8f0;
    --danger:#e2475c;
    --photo-warm:#c9b08a;
    --photo-cool:#a9abb2;
  }
  *{box-sizing:border-box;margin:0;padding:0}
  html,body{width:1200px;height:1200px;overflow:hidden}
  body{background:var(--bg);font-family:"Inter",sans-serif;color:var(--ink);
    display:flex;justify-content:center;align-items:center;gap:90px}
  .screen{width:390px;height:844px;background:var(--screen);border-radius:46px;
    overflow:hidden;position:relative;box-shadow:0 0 0 1px rgba(0,0,0,.06)}
  .status-bar{height:50px;display:flex;align-items:center;justify-content:space-between;padding:10px 28px 0 34px}
  .status-bar .time{font-size:16px;font-weight:600}
  .status-icons{display:flex;gap:6px;align-items:center}
  .nav-bar{height:50px;display:grid;grid-template-columns:70px 1fr 90px;align-items:center;
    padding:0 16px 0 22px;border-bottom:1px solid var(--line)}
  .nav-title{text-align:center;font-size:17px;font-weight:500}
  .save-draft{text-align:right;font-size:15px;font-weight:500;color:var(--link)}
  .form{padding:22px 28px 0}
  .form h1{font-size:21px;font-weight:600;margin-bottom:16px}
  .field-label{font-size:13px;font-weight:600;color:var(--label);margin-bottom:6px;display:block}
  .req{color:var(--danger);margin-left:2px}
  .field{margin-bottom:16px}
  .input{height:50px;border:1px solid var(--line);border-radius:12px;background:var(--field);
    display:flex;align-items:center;justify-content:space-between;padding:0 16px;font-size:15px}
  .upload-zone{height:74px;border:1.5px dashed var(--upload-line);background:var(--upload-bg);
    border-radius:2px;display:flex;align-items:center;justify-content:center;
    color:var(--upload-ink);font-size:15px;font-weight:500}
  .cover-photo{height:196px;background:linear-gradient(135deg,var(--photo-cool),var(--photo-warm))}
  .help{font-size:11.5px;color:var(--muted);line-height:1.5;margin-top:8px}
  .ingredients{border:1px solid var(--line);border-radius:10px;background:var(--field);overflow:hidden}
  .ingredients table{width:100%;border-collapse:collapse;font-size:12.5px}
  .ingredients th{font-weight:400;color:var(--muted);text-align:left;height:32px;padding-left:9px}
  .ingredients td{height:37px;padding-left:9px;border-top:1px solid var(--line)}
  .ingredients td.del{width:34px;padding:0}
  .add-link{display:block;font-size:12.5px;color:var(--link);margin:10px 8px 14px}
  .step-card{border:1px solid var(--line);border-radius:12px;background:var(--field);padding:12px 9px 12px}
  .step-card .step-text{font-size:12.5px;color:var(--muted);margin-bottom:12px}
  .step-card .upload-zone{height:66px}
  .home-indicator{position:absolute;bottom:8px;left:50%;transform:translateX(-50%);
    width:134px;height:5px;border-radius:3px;background:#111}
</style>
</head>
<body>

<svg width="0" height="0" style="position:absolute">
  <defs>
    <symbol id="trash" viewBox="0 0 16 16"><path d="M3 4h10M6.5 4V2.8h3V4M4.3 4l.7 9.5h6l.7-9.5M6.7 7v4M9.3 7v4" fill="none" stroke="currentColor" stroke-width="1.2" stroke-linecap="round" stroke-linejoin="round"/></symbol>
    <symbol id="status" viewBox="0 0 74 14"><rect x="0" y="9" width="3" height="4" rx="1"/><rect x="5" y="6.5" width="3" height="6.5" rx="1"/><rect x="10" y="4" width="3" height="9" rx="1"/><rect x="15" y="1" width="3" height="12" rx="1"/><path d="M27 5.2a10 10 0 0 1 14 0l-1.5 1.5a8 8 0 0 0-11 0zM30 8.2a6 6 0 0 1 8 0l-1.5 1.5a4 4 0 0 0-5 0zM32.8 11a2 2 0 0 1 2.4 0L34 12.5z"/><rect x="48" y="1.5" width="22" height="11" rx="3" fill="none" stroke="currentColor" stroke-opacity=".4"/><rect x="50" y="3.5" width="18" height="7" rx="1.6"/><rect x="71" y="5" width="1.6" height="4" rx=".8" opacity=".4"/></symbol>
  </defs>
</svg>

<!-- Empty state -->
<section class="screen">
  <div class="status-bar"><span class="time">9:41</span><svg class="status-icons" width="74" height="14"><use href="#status"/></svg></div>
  <header class="nav-bar">
    <svg width="20" height="16" viewBox="0 0 20 16"><path d="M19 8H2M8 2L2 8l6 6" fill="none" stroke="#26272b" stroke-width="1.6" stroke-linecap="round" stroke-linejoin="round"/></svg>
    <div class="nav-title">New Recipe</div>
    <div class="save-draft">Save Draft</div>
  </header>
  <main class="form">
    <h1>Create New Recipe</h1>
    <div class="field"><span class="field-label">Recipe Title<span class="req">*</span></span>
      <div class="input">Enter your Recipe Title</div></div>
    <div class="field"><span class="field-label">Upload Cover image</span>
      <div class="upload-zone">Click here or drag file to upload</div>
      <p class="help">Supported file format:<br>PNG, JPG; Maximum file size: 10MB</p></div>
    <div class="field"><span class="field-label">Number of people<span class="req">*</span></span>
      <div class="input">00<svg width="12" height="8" viewBox="0 0 12 8"><path d="M1 1.5l5 5 5-5" fill="none" stroke="#6d6f75" stroke-width="1.4"/></svg></div></div>
    <span class="field-label">Ingredients<span class="req">*</span></span>
    <div class="ingredients"><table>
      <tr><th>Name</th><th>Quantity</th><th>Unit</th><th></th></tr>
      <tr><td>Salt</td><td>1</td><td>Gram</td><td class="del"><svg width="16" height="16" style="color:var(--danger)"><use href="#trash"/></svg></td></tr>
      <tr><td>Olive Oil</td><td>2</td><td>Tablespoon</td><td class="del"><svg width="16" height="16" style="color:var(--danger)"><use href="#trash"/></svg></td></tr>
    </table></div>
    <span class="add-link">+ Add Ingredient</span>
    <span class="field-label">Recipe Steps<span class="req">*</span></span>
    <div class="step-card">
      <p class="step-text">1 Write Step instructions</p>
      <div class="upload-zone">Click here or drag file to upload</div>
    </div>
  </main>
  <div class="home-indicator"></div>
</section>

<!-- Filled state -->
<section class="screen">
  <div class="status-bar"><span class="time">9:41</span><svg class="status-icons" width="74" height="14"><use href="#status"/></svg></div>
  <header class="nav-bar">
    <svg width="20" height="16" viewBox="0 0 20 16"><path d="M19 8H2M8 2L2 8l6 6" fill="none" stroke="#26272b" stroke-width="1.6" stroke-linecap="round" stroke-linejoin="round"/></svg>
    <div class="nav-title">New Recipe</div>
    <div class="save-draft">Save Draft</div>
  </header>
  <main class="form">
    <h1>Create New Recipe</h1>
    <div class="field"><span class="field-label">Recipe Title<span class="req">*</span></span>
      <div class="input">Pasta with Sausage, Basil, and Mustard</div></div>
    <div class="field"><span class="field-label">Upload Cover image</span>
      <div class="cover-photo" role="img" aria-label="Cover photo: bowls of rigatoni with sausage and basil on a grey marble table"></div>
      <p class="help">Supported file format:<br>PNG, JPG; Maximum file size: 10MB</p></div>
    <div class="field"><span class="field-label">Number of people<span class="req">*</span></span>
      <div class="input">2<svg width="12" height="8" viewBox="0 0 12 8"><path d="M1 1.5l5 5 5-5" fill="none" stroke="#6d6f75" stroke-width="1.4"/></svg></div></div>
    <span class="field-label">Ingredients<span class="req">*</span></span>
    <div class="ingredients"><table>
      <tr><th>Name</th><th>Quantity</th><th>Unit</th><th></th></tr>
      <tr><td>Rigatoni</td><td>PMX09812</td><td>Gram</td><td class="del"><svg width="16" height="16" style="color:var(--danger)"><use href="#trash"/></svg></td></tr>
      <tr><td>Rigatoni</td><td>PMX09812</td><td>Gram</td><td class="del"><svg width="16" height="16" style="color:var(--danger)"><use href="#trash"/></svg></td></tr>
    </table></div>
    <span class="add-link">+ Add Ingredient</span>
    <div class="step-card">
      <p class="step-text">1 Write Step instructions</p>
      <div class="upload-zone">Click here or drag file to upload</div>
    </div>
  </main>
</section>

</body>
</html>
```